Harbor Reel Works Needs A Web Layout Design
Aqua/Black/White used on the layout
Creative Brief
Entertainment
Harbor reel works is a company that deals with videography, photography, and dj services. It uses the colours of blue, black, and white. The logo that can be used can be either of the following : http://www.velmorafind.example/images/vendor/300/230/harbor-logo.jpg or http://img18.pixelnookhost.example/img18/2856/26226344958409311344955.jpg . You can put demo tabs for the menu for now because those are not committed upon, and the body should look professional for the niche that his business is.
I like the clean and professional look but i hate having a lack of creativity within the design . Also i want it to show that we are the best and that the person coming to our website HAS TO GO WITH US, based on a POP of our website to their eye.
High Tech
aqua blue

```html
<!DOCTYPE html>
<html lang="en">
<head>
<meta charset="utf-8">
<title>Harbor Reel Works</title>
<link href="https://fonts.googleapis.com/css2?family=Ubuntu:wght@400;500;700&display=swap" rel="stylesheet">
<style>
  :root {
    --aqua: #2fc4d6;
    --aqua-bright: #6fe6f2;
    --aqua-deep: #0b5f6c;
    --teal-dark: #06343c;
    --ink: #020708;
    --panel: #050b0d;
    --white: #ffffff;
    --muted: #b9d6da;
    --tab-light: #e9f3f4;
  }
  * { margin: 0; padding: 0; box-sizing: border-box; }
  html, body { width: 1200px; height: 974px; overflow: hidden; background: var(--ink); }
  body { font-family: "Ubuntu", Arial, sans-serif; color: var(--white); position: relative; }

  .backdrop { position: absolute; inset: 0; }

  .brand {
    position: absolute; left: 520px; top: 10px; width: 160px; height: 96px;
    display: flex; flex-direction: column; align-items: center; justify-content: center; gap: 8px;
  }
  .brand-mark { width: 30px; height: 30px; background: var(--aqua); border-radius: 3px; }
  .brand-name { font-size: 15px; font-weight: 700; letter-spacing: 2px; color: var(--aqua-bright); text-align: center; line-height: 1.1; }

  .main-nav {
    position: absolute; left: 200px; top: 120px; width: 800px; height: 36px;
    display: flex; align-items: center; justify-content: space-between; padding: 0 12px;
    border-top: 1px solid rgba(111,230,242,.25); border-bottom: 1px solid rgba(111,230,242,.25);
  }
  .main-nav a { font-size: 15px; font-weight: 700; color: var(--aqua-bright); text-decoration: none; letter-spacing: .3px; }
  .main-nav a.current { color: var(--white); }

  .slider {
    position: absolute; left: 205px; top: 184px; width: 790px; height: 324px;
    border: 3px solid var(--aqua); background: var(--panel); overflow: visible;
  }
  .slide-photo {
    position: absolute; left: 10px; top: 10px; width: 764px; height: 298px;
    background: radial-gradient(ellipse at 35% 55%, #5b4432 0%, #2a1d14 35%, #0b0806 70%, #050403 100%);
  }
  .slide-caption { position: absolute; left: 424px; top: 112px; width: 330px; }
  .slide-caption h2 { font-size: 27px; font-weight: 700; margin-bottom: 10px; }
  .slide-caption p { font-size: 14.5px; font-weight: 700; line-height: 1.3; }
  .slide-arrow {
    position: absolute; top: 130px; width: 40px; height: 60px; background: var(--aqua);
    display: flex; align-items: center; justify-content: center;
  }
  .slide-arrow.prev { left: -3px; border-radius: 0 30px 30px 0; }
  .slide-arrow.next { right: -3px; border-radius: 30px 0 0 30px; }

  .showcase {
    position: absolute; left: 205px; top: 534px; width: 790px; height: 256px;
    border: 3px solid var(--aqua); border-top: none; background: var(--panel);
  }
  .tabs { display: flex; height: 40px; }
  .tab {
    flex: 1; display: flex; align-items: center; justify-content: center;
    font-size: 14px; font-weight: 700; background: var(--tab-light); color: var(--aqua-deep);
    border-top: 3px solid var(--aqua);
  }
  .tab.active { background: var(--panel); color: var(--white); border-right: 3px solid var(--aqua); border-left: 3px solid var(--aqua); }
  .tab + .tab { border-left: 2px solid var(--aqua); }
  .releases { position: absolute; top: 69px; left: 29px; width: 726px; height: 171px; display: flex; justify-content: space-between; }
  .release { width: 205px; height: 171px; border: 2px solid #e6e6e6; }
  .release.one { background: linear-gradient(160deg, #f0e2b8, #e7a79b 55%, #c9464a); }
  .release.two { background: linear-gradient(180deg, #8a7d74, #5c544f 60%, #3b3633); }
  .release.three { background: linear-gradient(160deg, #f0b54a, #b7453b 55%, #4a1e1c); }
  .side-arrow { position: absolute; top: 612px; width: 22px; height: 96px; }
  .side-arrow.prev { left: 183px; }
  .side-arrow.next { left: 995px; }

  .site-footer { position: absolute; left: 205px; top: 868px; width: 790px; height: 90px; font-size: 11px; color: var(--white); }
  .footer-brand {
    position: absolute; left: 0; top: 0; width: 118px; height: 52px;
    display: flex; flex-direction: column; align-items: center; justify-content: center; gap: 4px;
  }
  .footer-brand .brand-mark { width: 16px; height: 16px; }
  .footer-brand .brand-name { font-size: 10px; letter-spacing: 1px; }
  .copyright { position: absolute; left: 138px; top: 6px; line-height: 1.35; font-size: 10.5px; }
  .footer-col { position: absolute; top: 6px; list-style: none; line-height: 1.4; }
  .footer-col a { color: var(--white); text-decoration: none; }
  .col-a { left: 348px; } .col-b { left: 450px; } .col-c { left: 571px; } .col-social { left: 695px; }
  .social-row { display: flex; gap: 7px; margin-top: 4px; }
  .social-row span { width: 22px; height: 22px; border-radius: 3px; }
</style>
</head>
<body>
  <svg class="backdrop" width="1200" height="974" viewBox="0 0 1200 974" aria-hidden="true">
    <defs>
      <radialGradient id="topGlow" cx="600" cy="30" r="640" gradientUnits="userSpaceOnUse">
        <stop offset="0" stop-color="#3fc9d8"/>
        <stop offset="0.35" stop-color="#0d6b78"/>
        <stop offset="1" stop-color="#010405"/>
      </radialGradient>
      <radialGradient id="bottomGlow" cx="600" cy="1000" r="700" gradientUnits="userSpaceOnUse">
        <stop offset="0" stop-color="#1a8797"/>
        <stop offset="0.5" stop-color="#073a43"/>
        <stop offset="1" stop-color="#010405"/>
      </radialGradient>
    </defs>
    <rect width="1200" height="974" fill="#020708"/>
    <path d="M0 0 H1200 V150 Q600 230 0 150 Z" fill="url(#topGlow)"/>
    <path d="M0 110 Q600 250 1200 110" stroke="#6fe6f2" stroke-opacity=".35" stroke-width="2" fill="none"/>
    <path d="M0 60 Q600 180 1200 60" stroke="#6fe6f2" stroke-opacity=".15" stroke-width="1.5" fill="none"/>
    <path d="M0 974 V860 Q600 760 1200 860 V974 Z" fill="url(#bottomGlow)"/>
    <path d="M0 855 Q600 755 1200 855" stroke="#6fe6f2" stroke-opacity=".4" stroke-width="2" fill="none"/>
    <path d="M0 820 Q600 745 1200 820" stroke="#6fe6f2" stroke-opacity=".15" stroke-width="1.5" fill="none"/>
  </svg>

  <header class="brand">
    <span class="brand-mark"></span>
    <span class="brand-name">HARBOR REEL WORKS</span>
  </header>

  <nav class="main-nav">
    <a class="current" href="#">HOME</a>
    <a href="#">SERVICES</a>
    <a href="#">VIDEOGRAPHY</a>
    <a href="#">PHOTOGRAPHY</a>
    <a href="#">DJ SERVICES</a>
    <a href="#">CONTACT US</a>
  </nav>

  <section class="slider">
    <div class="slide-photo" role="img" aria-label="DJ performing at a turntable deck under warm stage lights"></div>
    <div class="slide-caption">
      <h2>Neque porro quisquam</h2>
      <p>Lorem ipsum dolor sit amet, consectetur adipiscing elit. Nam hendrerit ligula at odio scelerisque vel lobortis magna</p>
    </div>
    <div class="slide-arrow prev"><svg width="16" height="20" viewBox="0 0 16 20"><path d="M13 2 L3 10 L13 18 Z" fill="#fff"/></svg></div>
    <div class="slide-arrow next"><svg width="16" height="20" viewBox="0 0 16 20"><path d="M3 2 L13 10 L3 18 Z" fill="#fff"/></svg></div>
  </section>

  <section class="showcase">
    <div class="tabs">
      <div class="tab active">NEW RELEASES</div>
      <div class="tab">LATEST NEWS</div>
      <div class="tab">OUR SERVICES</div>
    </div>
    <div class="releases">
      <div class="release one" role="img" aria-label="Colourful release artwork with a performer and roses"></div>
      <div class="release two" role="img" aria-label="Release cover of an artist sitting by a brick wall"></div>
      <div class="release three" role="img" aria-label="Bright orange release cover of a singer"></div>
    </div>
  </section>
  <svg class="side-arrow prev" viewBox="0 0 22 96" aria-hidden="true"><path d="M22 0 V96 L0 48 Z" fill="#2fc4d6"/></svg>
  <svg class="side-arrow next" viewBox="0 0 22 96" aria-hidden="true"><path d="M0 0 V96 L22 48 Z" fill="#2fc4d6"/></svg>

  <footer class="site-footer">
    <div class="footer-brand">
      <span class="brand-mark"></span>
      <span class="brand-name">HARBOR REEL WORKS</span>
    </div>
    <p class="copyright">©2011 Harbor Reel Works.<br>All Rights Reserved.<br>Terms of use | Privacy Policy</p>
    <ul class="footer-col col-a"><li><a href="#">Home</a></li><li><a href="#">Services</a></li><li><a href="#">News</a></li></ul>
    <ul class="footer-col col-b"><li><a href="#">Videography</a></li><li><a href="#">Photography</a></li><li><a href="#">DJ Services</a></li></ul>
    <ul class="footer-col col-c"><li><a href="#">New Releases</a></li><li><a href="#">Testimonials</a></li><li><a href="#">Contact Us</a></li></ul>
    <div class="footer-col col-social">
      <div>Social Networks</div>
      <div class="social-row">
        <span style="background:#3b62b0"></span>
        <span style="background:#c9372c"></span>
        <span style="background:#4fb3e6"></span>
      </div>
    </div>
  </footer>
</body>
</html>
```